Quillon Energy Business Cards

I would like to design some options for about 10 sets of double sided business cards for our team with a raised logo with a Silver glossy finished logo. We are a privately funded upstream Oil & Gas producer drilling vertical wells in Central Oklahoma with a long term production (ROI driven) strategy that we implement through an annual drilling program. We are focused on a shallow / vertical / long life / low decline strategy. We are based in downtown Tulsa Oklahoma. I have attached a sample business card and a picture of our hallway logo which we would like to replicate on the business cards.

Target Market(s)

BRQ Accredited Investors and other Oil & Gas Operators

Industry/Entity Type

Upstream Oil & Gas

Contact Information for Business Card

You can see the sample photo attached, but email / website / address / direct phone / Cell Phone / Name / Title / Fax

Font styles to use
Other font styles liked:
• Felix Titling

Colors
0054AA
0677BA
7BADD7
CADEEF
E8F1F8

Requirements
Must have
• Glossy raised logo
Nice to have
• Possibly a new logo.
Should not have
• No Greens /

```html
<!DOCTYPE html>
<html lang="en">
<head>
<meta charset="utf-8">
<title>Quillon Energy Business Cards</title>
<link href="https://fonts.googleapis.com/css2?family=Marcellus+SC&display=swap" rel="stylesheet">
<style>
  :root {
    --blue-deep: #0054AA;
    --blue-mid: #0677BA;
    --blue-soft: #7BADD7;
    --blue-pale: #CADEEF;
    --blue-mist: #E8F1F8;
    --ink: #1c1c1c;
    --silver: #8a8d92;
    --card: #ffffff;
    --backdrop: #c9cacc;
  }
  * { margin: 0; padding: 0; box-sizing: border-box; }
  html, body { width: 1200px; height: 801px; overflow: hidden; }
  body {
    background: var(--backdrop);
    font-family: "Marcellus SC", "Times New Roman", serif;
    color: var(--ink);
    position: relative;
  }
  .card {
    position: absolute;
    top: 246px;
    width: 540px;
    height: 309px;
    background: var(--card);
    box-shadow: 0 6px 18px rgba(0,0,0,0.18);
  }
  .card--front { left: 40px; }
  .card--back { left: 620px; }

  .front-wordmark {
    position: absolute;
    left: 22px;
    top: 112px;
    width: 150px;
    text-align: center;
    color: var(--blue-deep);
    font-size: 24px;
    line-height: 1.15;
    letter-spacing: 1px;
  }
  .accent-rule {
    position: absolute;
    left: 190px;
    top: 44px;
    width: 14px;
    height: 230px;
  }
  .details {
    position: absolute;
    left: 222px;
    top: 42px;
    right: 18px;
  }
  .details__name {
    color: var(--blue-deep);
    font-size: 20px;
    letter-spacing: 0.5px;
    line-height: 1.1;
  }
  .details__title {
    font-size: 11.5px;
    line-height: 1.3;
    margin-top: 4px;
  }
  .details__address {
    font-size: 11.5px;
    line-height: 1.35;
    margin-top: 12px;
  }
  .contact-list {
    list-style: none;
    margin-top: 10px;
    font-size: 12px;
    letter-spacing: 1px;
  }
  .contact-list li {
    display: flex;
    align-items: center;
    gap: 8px;
    height: 17px;
  }
  .contact-list svg {
    width: 12px;
    height: 12px;
    fill: var(--blue-deep);
    flex: none;
  }

  .back-wordmark {
    position: absolute;
    left: 0;
    right: 0;
    top: 138px;
    text-align: center;
    color: var(--silver);
    font-size: 30px;
    letter-spacing: 1.5px;
  }
</style>
</head>
<body>

<section class="card card--front" aria-label="Business card front">
  <div class="front-wordmark">Quillon<br>Energy</div>

  <svg class="accent-rule" viewBox="0 0 14 230" aria-hidden="true">
    <rect x="0" y="0" width="4" height="230" fill="#0054AA"/>
    <rect x="5" y="0" width="3" height="230" fill="#0677BA"/>
    <rect x="9" y="0" width="2.5" height="230" fill="#7BADD7"/>
    <rect x="12" y="0" width="2" height="230" fill="#CADEEF"/>
  </svg>

  <div class="details">
    <div class="details__name">Dorian K. Halvorsen, CPL</div>
    <div class="details__title">Executive Vice President<br>Land, Legal &amp; Business Development</div>
    <div class="details__address">22 East 4th Street<br>Suite 900<br>Tulsa, OK 74103</div>
    <ul class="contact-list">
      <li>
        <svg viewBox="0 0 12 12"><path d="M2.5 0.5 L4.5 0.5 L5.2 3.2 L3.8 4.2 Q5 7 7.8 8.2 L8.8 6.8 L11.5 7.5 L11.5 9.5 Q11 11.5 9 11.5 Q1 10.5 0.5 3 Q0.5 1 2.5 0.5Z"/></svg>
        539-555-0142
      </li>
      <li>
        <svg viewBox="0 0 12 12"><path d="M3 0 H9 V12 H3Z M4 1.5 V9 H8 V1.5Z"/><circle cx="6" cy="10.5" r="0.7" fill="#fff"/></svg>
        918-555-0178
      </li>
      <li>
        <svg viewBox="0 0 12 12"><path d="M3 0 H9 V4 H3Z M0.5 4.5 H11.5 V11.5 H0.5Z"/><rect x="2" y="6" width="8" height="1" fill="#fff"/><rect x="2" y="8.5" width="8" height="1" fill="#fff"/></svg>
        918-555-0193
      </li>
      <li>
        <svg viewBox="0 0 12 12"><path d="M0 2 H12 V10 H0Z"/><path d="M0.5 2.5 L6 7 L11.5 2.5" stroke="#fff" stroke-width="1" fill="none"/></svg>
        DKH@qetulsa.com
      </li>
      <li>
        <svg viewBox="0 0 12 12"><circle cx="6" cy="6" r="5.5"/><g stroke="#fff" stroke-width="0.8" fill="none"><ellipse cx="6" cy="6" rx="2.5" ry="5.5"/><line x1="0.5" y1="6" x2="11.5" y2="6"/><line x1="1.5" y1="3.3" x2="10.5" y2="3.3"/><line x1="1.5" y1="8.7" x2="10.5" y2="8.7"/></g></svg>
        www.quillonenergyllc.com
      </li>
    </ul>
  </div>
</section>

<section class="card card--back" aria-label="Business card back">
  <div class="back-wordmark">Quillon Energy, LLC</div>
</section>

</body>
</html>
```